Marlowe Bay Consulting Business Card

Hi Corvel. Thank you for your work on my coaching business card. I have another business which needs a new card. It is my counselling business. The best way to find out how to approach this project will be to go to my other website. www.marlowebayconsulting.com.au and you will be able to see the colours scheme that I will require. White, Green and blue.

The tag line is Marlowe Bay Consulting So you can look forward to tomorrow. The clients are varied but mostly middle class Australian. The card is to show on it the same details as my other business card but with a different phone number. The tag lines are obviously different. The phone number is 9137 5264 The addresses are all the same.

Again simple, professional sophisticated is best.

```html
<!DOCTYPE html>
<html lang="en">
<head>
<meta charset="utf-8">
<title>Marlowe Bay Consulting – Business Card</title>
<link rel="stylesheet" href="https://fonts.googleapis.com/css2?family=Open+Sans:wght@400;600;700&display=swap">
<style>
  :root {
    --backdrop: #d8d9db;
    --card: #f5f6f7;
    --blue: #1f6fc4;
    --blue-deep: #1658a9;
    --blue-light: #3d8ee0;
    --green: #3f9a4a;
    --ink: #3b3b3b;
    --ink-soft: #555a60;
    --rule: #c9ccd1;
  }
  * { box-sizing: border-box; margin: 0; padding: 0; }
  html, body {
    width: 1200px; height: 1005px; overflow: hidden;
    background: var(--backdrop);
    font-family: "Open Sans", Arial, sans-serif;
  }
  .canvas {
    position: relative; width: 1200px; height: 1005px;
    display: flex; flex-direction: column; align-items: center; justify-content: center; gap: 34px;
  }
  .card {
    position: relative; width: 800px; height: 457px;
    background: var(--card);
    box-shadow: 0 6px 18px rgba(0,0,0,.18);
    overflow: hidden;
  }

  /* Back of card */
  .card--back { display: flex; flex-direction: column; align-items: center; justify-content: center; }
  .card--back .brand { font-size: 40px; }
  .tagline { margin-top: 12px; font-size: 18px; font-style: normal; color: var(--green); letter-spacing: .02em; }
  .site { margin-top: 30px; font-size: 20px; color: var(--ink); }

  /* Brand lockup */
  .brand { display: flex; align-items: center; gap: 14px; color: var(--blue-deep); font-weight: 600; letter-spacing: .05em; white-space: nowrap; }
  .brand__dot { width: .6em; height: .6em; border-radius: 50%; background: var(--green); flex: none; }

  /* Front of card */
  .band { position: absolute; left: 0; right: 0; top: 100px; height: 16px; background: var(--blue); }
  .name-tab {
    position: absolute; left: 0; top: 44px; width: 340px; height: 72px;
    background: linear-gradient(180deg, var(--blue-light), var(--blue));
    border-top-right-radius: 34px 72px;
    padding: 12px 0 0 36px;
    color: #fff; font-weight: 700; font-size: 29px; letter-spacing: .02em; text-transform: uppercase;
  }
  .role { position: absolute; left: 356px; top: 64px; font-weight: 700; font-size: 21px; color: var(--ink-soft); }

  .contacts { position: absolute; left: 0; top: 140px; width: 430px; list-style: none; }
  .contact { position: relative; display: flex; align-items: flex-start; gap: 30px; padding: 12px 0 14px 38px; font-size: 19px; line-height: 1.3; color: var(--ink); }
  .contact + .contact::before { content: ""; position: absolute; left: 0; top: 0; width: 150px; height: 1px; background: var(--rule); }
  .contact svg { width: 26px; height: 26px; flex: none; fill: var(--blue); margin-top: 1px; }

  .card--front .brand { position: absolute; right: 44px; top: 255px; font-size: 26px; }
</style>
</head>
<body>
<main class="canvas">
  <section class="card card--back" aria-label="Card back">
    <div class="brand"><span class="brand__dot"></span>Marlowe Bay Consulting</div>
    <p class="tagline">So you can look forward to tomorrow</p>
    <p class="site">www.marlowebayconsulting.com.au</p>
  </section>

  <section class="card card--front" aria-label="Card front">
    <div class="band"></div>
    <h1 class="name-tab">Hollis Verane</h1>
    <p class="role">Managing Director</p>

    <ul class="contacts">
      <li class="contact">
        <svg viewBox="0 0 24 24" aria-hidden="true"><path d="M12 1.5a7.5 7.5 0 0 0-7.5 7.5c0 5.6 7.5 13.5 7.5 13.5s7.5-7.900 7.5-13.5A7.5 7.5 0 0 0 12 1.5zm0 10.3a2.8 2.8 0 1 1 0-5.6 2.8 2.8 0 0 1 0 5.6z"/></svg>
        <span>Level 4, 27 Tidewater Lane<br>Marlowe Bay</span>
      </li>
      <li class="contact">
        <svg viewBox="0 0 24 24" aria-hidden="true"><path d="M6.6 10.8a15.1 15.1 0 0 0 6.6 6.6l2.2-2.2a1 1 0 0 1 1-.25 11.4 11.4 0 0 0 3.6.57 1 1 0 0 1 1 1V20a1 1 0 0 1-1 1A17 17 0 0 1 3 4a1 1 0 0 1 1-1h3.5a1 1 0 0 1 1 1c0 1.25.2 2.45.57 3.6a1 1 0 0 1-.25 1z"/></svg>
        <span>9137 5264<br>9137 5264</span>
      </li>
      <li class="contact">
        <svg viewBox="0 0 24 24" aria-hidden="true"><path d="M2 5h20v14H2zm2 2v.4l8 5.2 8-5.2V7zm0 2.8V17h16V9.8l-8 5.2z"/></svg>
        <span>hello@marlowebay.com.au</span>
      </li>
      <li class="contact">
        <svg viewBox="0 0 24 24" aria-hidden="true"><path d="M12 2a10 10 0 1 0 0 20 10 10 0 0 0 0-20zm6.9 6h-3a15.6 15.6 0 0 0-1.3-3.9A8 8 0 0 1 18.9 8zM12 4c.8 1.1 1.5 2.5 1.9 4h-3.8c.4-1.5 1.1-2.9 1.9-4zM4.3 14a8 8 0 0 1 0-4h3.4a16 16 0 0 0 0 4zm.8 2h3a15.6 15.6 0 0 0 1.3 3.9A8 8 0 0 1 5.1 16zm3-8h-3a8 8 0 0 1 4.3-3.9A15.6 15.6 0 0 0 8.1 8zM12 20c-.8-1.1-1.5-2.5-1.9-4h3.8c-.4 1.5-1.1 2.9-1.9 4zm2.3-6H9.7a14 14 0 0 1 0-4h4.6a14 14 0 0 1 0 4zm.3 5.9a15.6 15.6 0 0 0 1.3-3.9h3a8 8 0 0 1-4.3 3.9zm1.7-5.9a16 16 0 0 0 0-4h3.4a8 8 0 0 1 0 4z"/></svg>
        <span>www.marlowebayconsulting.com.au</span>
      </li>
    </ul>

    <div class="brand"><span class="brand__dot"></span>Marlowe Bay Consulting</div>
  </section>
</main>
</body>
</html>
```